Brightpath Holdings Business Card

Create a two sided, high gloss, quality business card for Brightpath Holdings.

Target Market(s)

People wanting to purchase, scale, and sell businesses.

Industry/Entity Type

Entrepreneurs

Contact Information for Business Card

One line: Dana Velko, CPA, CMA Another line: Entrepreneur & Investor Another line: Business Ownership Transition Expert Another line: Multi-State Licensed Real Estate Broker Phone 954-BRTPATH (278-7284) Email Dana@Brightpath Holdings.example Website www.Brightpath.example

Requirements
Must have
• Black Card, logo on one side, all other information on the other side including a small logo.
Nice to have
• Possibly add a tagline "Helping entrepreneurs live a life they don't need a vacation from"
Should not have
• There will not be a mailing address on these cards.

```html
<!DOCTYPE html>
<html lang="en">
<head>
<meta charset="utf-8">
<title>Brightpath Holdings Business Card</title>
<link href="https://fonts.googleapis.com/css2?family=Open+Sans:wght@400;700;800&display=swap" rel="stylesheet">
<style>
  :root {
    --backdrop: #222223;
    --card: #1d1d20;
    --gold: #d9b445;
    --gold-light: #f3dc8a;
    --gold-deep: #a9821f;
    --ink-light: #f2f2f2;
  }
  * { box-sizing: border-box; margin: 0; padding: 0; }
  html, body {
    width: 1200px; height: 780px; overflow: hidden;
    background: var(--backdrop);
    font-family: "Open Sans", Arial, sans-serif;
  }
  .sheet { position: relative; width: 1200px; height: 780px; }
  .card {
    position: absolute; top: 225px;
    width: 525px; height: 300px;
    background: var(--card);
    box-shadow: 0 18px 40px rgba(0,0,0,.55);
    overflow: hidden;
  }
  .card--info { left: 50px; }
  .card--brand { left: 625px; }

  .wordmark {
    color: var(--gold);
    font-weight: 800;
    line-height: 1.05;
    display: flex; align-items: center; gap: 10px;
  }
  .wordmark__dot {
    width: 12px; height: 12px; border-radius: 50%;
    background: var(--gold); flex: none;
  }
  .card--info .wordmark {
    position: absolute; left: 70px; top: 48px;
    font-size: 26px;
  }
  .card--brand .wordmark {
    position: absolute; left: 0; right: 0; top: 0; bottom: 0;
    justify-content: center; font-size: 44px;
  }

  .contact {
    position: absolute; left: 26px; top: 222px;
    list-style: none;
    color: var(--ink-light); font-size: 12.5px; line-height: 18px;
  }
  .contact li { display: flex; align-items: center; gap: 8px; }
  .contact svg { width: 11px; height: 11px; fill: var(--gold); flex: none; }

  .person {
    position: absolute; right: 38px; top: 112px;
    text-align: right;
  }
  .person__name {
    font-size: 30px; font-weight: 700; line-height: 1.1;
    background: linear-gradient(180deg, var(--gold-light), var(--gold) 55%, var(--gold-deep));
    -webkit-background-clip: text; background-clip: text; color: transparent;
    margin-bottom: 6px;
  }
  .person__titles {
    color: var(--ink-light); font-size: 13px; line-height: 18px;
  }

  .gold-tab {
    position: absolute; right: 0; top: 170px;
    width: 14px; height: 80px;
    background: linear-gradient(90deg, var(--gold-deep), var(--gold-light) 50%, var(--gold));
  }
</style>
</head>
<body>
<main class="sheet">

  <section class="card card--info" aria-label="Business card, information side">
    <div class="wordmark"><span class="wordmark__dot"></span>Brightpath Holdings</div>

    <div class="person">
      <h1 class="person__name">Dana Velko</h1>
      <p class="person__titles">
        CPA, CPA, Entrepreneur, Investor,<br>
        Business Ownership Transition Expert,<br>
        Multi-State Licensed Real Estate Broker
      </p>
    </div>

    <ul class="contact">
      <li>
        <svg viewBox="0 0 24 24" aria-hidden="true"><path d="M6.6 10.8a15.1 15.1 0 0 0 6.6 6.6l2.2-2.2c.3-.3.7-.4 1-.2 1.1.4 2.3.6 3.6.6.6 0 1 .4 1 1V20c0 .6-.4 1-1 1A17 17 0 0 1 3 4c0-.6.4-1 1-1h3.5c.6 0 1 .4 1 1 0 1.3.2 2.5.6 3.6.1.3 0 .7-.2 1z"/></svg>
        555-214-0193
      </li>
      <li>
        <svg viewBox="0 0 24 24" aria-hidden="true"><path d="M2 5h20v14H2zm2 2v.5l8 5 8-5V7zm0 2.8V17h16V9.8l-8 5z"/></svg>
        Dana@Brightpath Holdings.example
      </li>
      <li>
        <svg viewBox="0 0 24 24" aria-hidden="true"><path d="M12 2a10 10 0 1 0 0 20 10 10 0 0 0 0-20zm6.9 9h-3a15 15 0 0 0-1.3-5.9A8 8 0 0 1 18.9 11zM12 4c.9 1.2 1.8 3.6 1.9 7h-3.8c.1-3.4 1-5.8 1.9-7zM9.4 5.1A15 15 0 0 0 8.1 11h-3a8 8 0 0 1 4.3-5.9zM5.1 13h3a15 15 0 0 0 1.3 5.9A8 8 0 0 1 5.1 13zM12 20c-.9-1.2-1.8-3.6-1.9-7h3.8c-.1 3.4-1 5.8-1.9 7zm2.6-1.1a15 15 0 0 0 1.3-5.9h3a8 8 0 0 1-4.3 5.9z"/></svg>
        www.Dana@Brightpath Holdings.example
      </li>
    </ul>

    <div class="gold-tab" aria-hidden="true"></div>
  </section>

  <section class="card card--brand" aria-label="Business card, logo side">
    <div class="wordmark"><span class="wordmark__dot"></span>Brightpath Holdings</div>
  </section>

</main>
</body>
</html>
```